3D Printing Business coming soon page

Hi we are looking for a one page "coming soon" website for our business. The business is called "Solevia Labs" and it is a new solution which 3D Prints Orthotics (Insoles).

The design should include our logo, an improved version of our promotional image (attached), a web form for capturing interest from people, a countdown timer and some text.

Follow the colour scheme which is shown in our logo along with our other colours - Orange (RGB#ff8300) and Light Green (RGB#30f20a)
Updates

Industry/Entity Type

Business

Font styles to use
Sans Serif

Requirements
Must have
• Logo (Attached)
Improved version of Promotional Image
Web Form design for capturing Name, EMail Address and Comments along with a Turin test
Countdown Timer
Text - "Solevia Labs will shake up the Orthotics Industry. Foot Orthosis patient-ready in hours for a fraction of the price you are paying today. Welcome to the new world of 3D Printing!"

```html
<!DOCTYPE html>
<html lang="en">
<head>
<meta charset="utf-8">
<title>Solevia Labs — Coming Soon</title>
<link href="https://fonts.googleapis.com/css2?family=Roboto:wght@300;400&family=Open+Sans:wght@400;600&display=swap" rel="stylesheet">
<style>
  :root{
    --bg-dark:#2b2b2b;
    --text-light:#e6e6e6;
    --white:#ffffff;
    --green:#30f20a;
    --orange:#ff8300;
    --blue:#0b6e99;
    --red:#ee2a2a;
    --step-green:#4f8a3a;
    --ring-dark:#0c0c0c;
    --bar-fill:#a8d40c;
    --nav-line:#9a9a9a;
    --logo-blue:#1a74c7;
    --field-bg:rgba(20,20,20,.75);
    --field-line:#5a5a5a;
  }
  *{margin:0;padding:0;box-sizing:border-box}
  html,body{width:1200px;height:750px;overflow:hidden;background:var(--bg-dark)}
  .page{position:relative;width:1200px;height:750px;font-family:"Roboto",sans-serif;color:var(--text-light);overflow:hidden}
  .hero-photo{position:absolute;inset:0;background:radial-gradient(ellipse at 45% 45%, #5c5a57 0%, #44423f 45%, #2a2a2a 100%)}
  .logo{position:absolute;top:56px;left:0;width:1200px;display:flex;justify-content:center;align-items:center;gap:10px}
  .logo-dot{width:24px;height:24px;border-radius:50%;background:var(--logo-blue)}
  .logo-name{font-family:"Roboto",sans-serif;font-weight:400;font-size:36px;color:var(--logo-blue)}
  .headline{position:absolute;top:133px;width:1200px;text-align:center;font-size:30px;font-weight:400;line-height:36px}
  .headline .green{color:var(--green)}
  .headline .orange{color:var(--orange)}
  .intro{position:absolute;top:177px;left:0;width:1200px;text-align:center;font-size:21.5px;font-weight:300;line-height:27.5px;color:var(--text-light);white-space:nowrap}
  .steps{position:absolute;top:302px;left:0;width:1200px;height:116px}
  .step{position:absolute;width:116px;height:116px;border-radius:50%;border:2px solid;background:rgba(110,110,110,.55);overflow:hidden;text-align:center;font-size:13.5px;line-height:15px;color:var(--white)}
  .step-label{position:relative;margin-top:16px;z-index:1}
  .step-art{position:absolute;left:26px;top:48px;width:60px;height:46px;border-radius:3px}
  .step-scan{left:295px;border-color:var(--step-green)}
  .step-scan .step-art{background:linear-gradient(#e8e8e8,#bdbdbd)}
  .step-design{left:460px;border-color:var(--orange)}
  .step-design .step-art{background:linear-gradient(#f4f4f4,#dcdcdc);width:74px;left:19px;top:52px;height:38px}
  .step-print{left:625px;border-color:var(--blue)}
  .step-print .step-art{background:linear-gradient(#d9d9d9,#a9a9b0);left:24px;top:42px;height:54px;width:66px}
  .step-fit{left:790px;border-color:var(--red)}
  .step-fit .step-art{left:0;top:0;width:116px;height:116px;border-radius:0;background:radial-gradient(circle at 60% 60%, #d9cdb0 0%, #6c6558 45%, #3b3a38 100%)}
  .step-fit .step-label{margin-top:20px}
  .step-arrow{position:absolute;top:46px}
  .nav{position:absolute;width:57px;height:57px}
  .nav-prev{left:42px;top:388px}
  .nav-next{left:1101px;top:346px}
  .coming{position:absolute;top:456px;width:1200px;text-align:center;font-family:"Open Sans",sans-serif;font-weight:400;font-size:31px;line-height:42px;color:var(--white)}
  .countdown{position:absolute;top:526px;left:0;width:1200px;height:118px}
  .unit{position:absolute;width:118px;height:118px}
  .unit svg{position:absolute;inset:0}
  .unit-value{position:absolute;top:22px;width:118px;text-align:center;font-family:"Open Sans",sans-serif;font-weight:600;font-size:39px;line-height:46px;color:var(--white)}
  .unit-label{position:absolute;top:73px;width:118px;text-align:center;font-family:"Roboto",sans-serif;font-size:12px;color:var(--white)}
  .progress{position:absolute;left:261px;top:664px;width:679px;height:23px;background:#1a1a1a;border:1px solid #3a3a3a}
  .progress-track{position:absolute;left:5px;top:6px;width:626px;height:9px;background:repeating-linear-gradient(115deg,#262626 0 14px,#333 14px 28px)}
  .progress-fill{position:absolute;left:0;top:0;width:30%;height:100%;background:var(--bar-fill)}
  .progress-value{position:absolute;right:10px;top:4px;font-size:9px;color:var(--white)}
  .footer-note{position:absolute;left:262px;top:710px;font-size:12px;line-height:14px;color:var(--text-light)}
  .interest-form{position:absolute;left:452px;top:705px;width:424px;height:24px;display:flex;align-items:center;gap:5px}
  .interest-form input{height:22px;border:1px solid var(--field-line);background:var(--field-bg);color:var(--white);font-family:"Roboto",sans-serif;font-size:11px;padding:0 6px;border-radius:2px}
  .interest-form input::placeholder{color:#b5b5b5}
  .field-name{width:78px}
  .field-email{width:92px}
  .field-comments{width:98px}
  .captcha-label{font-size:11px;color:var(--text-light);white-space:nowrap}
  .field-captcha{width:30px;text-align:center}
  .submit{height:22px;width:56px;border:0;border-radius:2px;background:var(--orange);color:var(--white);font-family:"Roboto",sans-serif;font-size:11px}
  .social{position:absolute;left:885px;top:705px;display:flex;gap:6px}
  .social span{width:23px;height:23px;border-radius:50%;background:var(--white)}
</style>
</head>
<body>
<main class="page">
  <div class="hero-photo" role="img" aria-label="Background photo of hands holding a custom insole next to a black shoe, dimmed"></div>

  <header class="logo">
    <span class="logo-dot"></span>
    <span class="logo-name">Solevia Labs</span>
  </header>

  <h1 class="headline"><span class="green">Our Website is</span> <span class="orange">Under Construction !</span></h1>
  <p class="intro">Solevia Labs will shake up the Orthotics Industry. Foot Orthosis<br>patient-ready in hours for a fraction of the price you are paying today.<br>Welcome to the new world of 3D Printing!</p>

  <section class="steps">
    <div class="step step-scan">
      <div class="step-label">Scan the<br>foot</div>
      <div class="step-art" role="img" aria-label="Foot scanning tablet"></div>
    </div>
    <svg class="step-arrow" style="left:422px" width="28" height="22" viewBox="0 0 28 22"><path d="M2 11H24M15 3l9 8-9 8" fill="none" stroke="#fff" stroke-width="3"/></svg>
    <div class="step step-design">
      <div class="step-label">Design the<br>orthotics</div>
      <div class="step-art" role="img" aria-label="Orthotic design software screen"></div>
    </div>
    <svg class="step-arrow" style="left:586px" width="28" height="22" viewBox="0 0 28 22"><path d="M2 11H24M15 3l9 8-9 8" fill="none" stroke="#fff" stroke-width="3"/></svg>
    <div class="step step-print">
      <div class="step-label">3D Print it</div>
      <div class="step-art" role="img" aria-label="3D printer"></div>
    </div>
    <svg class="step-arrow" style="left:750px" width="28" height="22" viewBox="0 0 28 22"><path d="M2 11H24M15 3l9 8-9 8" fill="none" stroke="#fff" stroke-width="3"/></svg>
    <div class="step step-fit">
      <div class="step-art" role="img" aria-label="Insole being fitted into a shoe"></div>
      <div class="step-label">Fit it</div>
    </div>
  </section>

  <svg class="nav nav-prev" viewBox="0 0 57 57" aria-label="Previous">
    <circle cx="28.5" cy="28.5" r="27" fill="none" stroke="var(--nav-line)" stroke-width="2"/>
    <path d="M13 29L40 14 33 29 40 44Z" fill="var(--nav-line)"/>
  </svg>
  <svg class="nav nav-next" viewBox="0 0 57 57" aria-label="Next">
    <circle cx="28.5" cy="28.5" r="27" fill="none" stroke="var(--nav-line)" stroke-width="2"/>
    <path d="M44 29L17 14 24 29 17 44Z" fill="var(--nav-line)"/>
  </svg>

  <h2 class="coming">Coming soon</h2>

  <section class="countdown">
    <div class="unit" style="left:295px">
      <svg viewBox="0 0 118 118"><circle cx="59" cy="59" r="51" fill="var(--ring-dark)" stroke="var(--ring-dark)" stroke-width="15"/><circle cx="59" cy="59" r="51" fill="none" stroke="var(--green)" stroke-width="15" stroke-dasharray="295 400" transform="rotate(-90 59 59)"/></svg>
      <div class="unit-value">99</div><div class="unit-label">DAYS</div>
    </div>
    <div class="unit" style="left:460px">
      <svg viewBox="0 0 118 118"><circle cx="59" cy="59" r="51" fill="var(--ring-dark)" stroke="var(--ring-dark)" stroke-width="15"/><circle cx="59" cy="59" r="51" fill="none" stroke="var(--orange)" stroke-width="15" stroke-dasharray="312 400" transform="rotate(-86 59 59)"/></svg>
      <div class="unit-value">12</div><div class="unit-label">HOURS</div>
    </div>
    <div class="unit" style="left:625px">
      <svg viewBox="0 0 118 118"><circle cx="59" cy="59" r="51" fill="var(--ring-dark)" stroke="var(--ring-dark)" stroke-width="15"/><circle cx="59" cy="59" r="51" fill="none" stroke="var(--blue)" stroke-width="15" stroke-dasharray="312 400" transform="rotate(-86 59 59)"/></svg>
      <div class="unit-value">30</div><div class="unit-label">MINUTES</div>
    </div>
    <div class="unit" style="left:790px">
      <svg viewBox="0 0 118 118"><circle cx="59" cy="59" r="51" fill="var(--ring-dark)" stroke="var(--ring-dark)" stroke-width="15"/><circle cx="59" cy="59" r="51" fill="none" stroke="var(--red)" stroke-width="15" stroke-dasharray="240 400" transform="rotate(-90 59 59)"/></svg>
      <div class="unit-value">59</div><div class="unit-label">SECONDS</div>
    </div>
  </section>

  <div class="progress">
    <div class="progress-track"><div class="progress-fill"></div></div>
    <span class="progress-value">30%</span>
  </div>

  <footer>
    <p class="footer-note">© Copyrights. All Rights Reserved</p>
    <form class="interest-form" action="#" method="post">
      <input class="field-name" type="text" name="name" placeholder="Name" aria-label="Name">
      <input class="field-email" type="email" name="email" placeholder="Email" aria-label="Email address">
      <input class="field-comments" type="text" name="comments" placeholder="Comments" aria-label="Comments">
      <label class="captcha-label" for="captcha">3 + 4 =</label>
      <input class="field-captcha" id="captcha" type="text" name="captcha" aria-label="Answer to check you are human">
      <button class="submit" type="submit">Notify me</button>
    </form>
    <div class="social"><span></span><span></span></div>
  </footer>
</main>
</body>
</html>
```